BHP Business Cards

I need business cards for "copper glen partners llc" doublesided... logo on the back (also include logo on front)
logo attached to project... i have jpg up.. let me know if you need eps file.
Company Info:
842 East Marlow Avenue, Suite 7B
Chicago, Illinois 60617
facsimile 312-555-4186 (list fax, address, website on all cards.)
www.copperglenpartnersllc.example
Three different people on cards:
Dorian K. Patel, CPA MST
Principal
ofc 312-555-0271
mobile 312-555-0388
doriankpatel@copperglenpartnersllc.example
Harold J. Quenby, CPA MST
Principal
haroldjquenby@copperglenpartnersllc.example
mobile 708-555-0149
ofc 312-555-0271
Miles T Carver
Principal
ofc 312-555-0271
no mobile
milestcarver@copperglenpartnersllc.example
I have multiple projects listed.. see below:
Business cards for copper glen partners llc
letterhead
envelopes
Business cards for KM Holdings LLC
letterhead
envelopes
rich people
Business

```html
<!DOCTYPE html>
<html lang="en">
<head>
<meta charset="utf-8">
<title>Copper Glen Partners LLC — Stationery</title>
<link rel="stylesheet" href="https://fonts.googleapis.com/css2?family=Arimo&family=Tinos:ital,wght@0,400;0,700;1,400&display=swap">
<style>
  :root {
    --backdrop: #6b6d70;
    --navy: #1c3253;
    --paper: #ffffff;
    --ink: #3a3a3a;
    --ink-soft: #8a8a8a;
    --on-navy: #ffffff;
  }
  * { margin: 0; padding: 0; box-sizing: border-box; }
  html, body { width: 927px; height: 1200px; overflow: hidden; }
  body { background: var(--backdrop); position: relative; font-family: "Tinos", "Times New Roman", serif; }

  .sheet { position: absolute; background: var(--paper); box-shadow: 2px 3px 8px rgba(0,0,0,.35); }

  /* Letterhead */
  .letterhead { left: 133px; top: 45px; width: 680px; height: 880px; }
  .letterhead-band { position: absolute; left: 11px; top: 11px; width: 659px; height: 83px; }
  .letterhead-contact { position: absolute; left: 496px; top: 25px; color: var(--on-navy); font-size: 10.5px; line-height: 13px; }
  .letterhead-brand { position: absolute; left: 22px; top: 66px; }

  .brand { display: flex; flex-direction: column; align-items: center; color: var(--navy); font-family: "Tinos", "Times New Roman", serif; font-weight: 400; text-transform: uppercase; letter-spacing: .5px; white-space: nowrap; }
  .brand-mark { border-radius: 50%; background: var(--navy); }
  .letterhead-brand .brand-mark { width: 54px; height: 54px; margin-bottom: 8px; }
  .letterhead-brand .brand-name { font-size: 13px; }

  .letter-salutation { position: absolute; left: 185px; top: 291px; font-family: "Arimo", Arial, sans-serif; font-size: 11px; color: var(--ink); }
  .letter-body { position: absolute; left: 185px; top: 358px; width: 387px; font-family: "Arimo", Arial, sans-serif; font-size: 8.4px; line-height: 13.5px; color: var(--ink); text-align: justify; }
  .letter-body p + p { margin-top: 13.5px; }
  .letter-closing { position: absolute; left: 185px; top: 673px; font-family: "Arimo", Arial, sans-serif; font-size: 8.4px; color: var(--ink-soft); }

  .contact-line b { font-weight: 700; display: inline-block; width: 26px; }

  /* Business card */
  .business-card { left: 603px; top: 177px; width: 311px; height: 159px; display: flex; }
  .card-front { width: 132px; height: 100%; display: flex; align-items: center; justify-content: center; }
  .card-front .brand-mark { width: 28px; height: 28px; margin-bottom: 5px; }
  .card-front .brand-name { font-size: 7px; }
  .card-details { flex: 1; background: var(--navy); color: var(--on-navy); padding: 20px 0 0 15px; font-size: 7px; line-height: 9px; }
  .card-name { font-weight: 700; font-size: 10.5px; line-height: 12px; }
  .card-title { font-style: italic; font-size: 6.5px; margin-bottom: 13px; }
  .card-details .contact-line b { width: 18px; }
  .card-web { margin-top: 12px; }

  /* Envelope */
  .envelope { left: 33px; top: 803px; width: 759px; height: 330px; }
  .envelope-brand { position: absolute; left: 30px; top: 16px; }
  .envelope-brand .brand-mark { width: 62px; height: 62px; margin-bottom: 10px; }
  .envelope-brand .brand-name { font-size: 15px; }
  .envelope-web { position: absolute; left: 550px; top: 34px; font-size: 13.5px; color: var(--navy); }
  .envelope-return { position: absolute; left: 28px; top: 247px; font-size: 10.5px; line-height: 13px; color: var(--ink); }
</style>
</head>
<body>

<section class="sheet letterhead">
  <svg class="letterhead-band" viewBox="0 0 659 83" aria-hidden="true">
    <path d="M0 0 H659 V83 H200 C150 83 130 30 80 30 H0 Z" fill="var(--navy)"/>
  </svg>
  <address class="letterhead-contact" style="font-style:normal">
    842 East Marlow Avenue, Suite 7B<br>
    Chicago, Illinois 60617<br>
    <span class="contact-line"><b>Tel.</b> 312.555.0271</span><br>
    <span class="contact-line"><b>Fax.</b> 312.555.4186</span><br>
    www.copperglenpartnersllc.example
  </address>
  <div class="letterhead-brand brand">
    <span class="brand-mark"></span>
    <span class="brand-name">Copper Glen Partners llc</span>
  </div>

  <p class="letter-salutation">Dear Mr. Hollis</p>
  <div class="letter-body">
    <p>Lorem ipsum dolor sit amet, consectetur adipiscing elit. Vestibulum adipiscing felis ac tortor consectetur feugiat. Etiam malesuada sodales eros ut ornare. Sed lorem eros, mattis id pretium ut, faucibus sit amet quam. Nullam consectetur ultricies ipsum, fringilla porttitor erat ornare at. Sed sit amet dui vel sapien ultrices vulputate. In hac habitasse platea dictumst. Nam est nisi, rhoncus at sagittis a, porttitor adipiscing nulla. Vivamus placerat felis ultrices quam iaculis eget dignissim felis egestas. Integer nec molestie lorem. Sed odio tellus, vulputate sed laoreet non, vulputate id justo. Etiam suscipit, odio vel auctor dictum, felis turpis ullamcorper neque, quis sodales risus metus in magna. Morbi pellentesque justo at quam laoreet facilisis. Aenean placerat, urna ornare aliquet tincidunt, lorem justo molestie ligula, id placerat est metus nec lectus. Nullam eu ipsum quis turpis tristique iaculis rutrum nec nibh. Phasellus risus eros, semper sit amet faucibus sit amet, laoreet at neque. Donec eros sem, viverra dictum faucibus quis, ullamcorper tincidunt nulla.</p>
    <p>Aenean ut congue tellus. Class aptent taciti sociosqu ad litora torquent per conubia nostra, per inceptos himenaeos. Sed facilisis, velit tincidunt pharetra fermentum, urna tortor iaculis erat, vitae sollicitudin leo mauris quis mi. Cras malesuada sem ac ipsum sagittis ultrices. Mauris fermentum porttitor nisi, eu facilisis lorem consectetur et. Suspendisse est elit, scelerisque ac euismod id, scelerisque viverra odio. Nullam scelerisque metus in eros semper congue. Fusce a fermentum est. Ut ac leo dolor. Quisque dignissim mauris a neque luctus pretium ultrices risus sagittis. Aenean quam massa, rutrum ac hendrerit eu, interdum eu nulla. Curabitur a velit mauris, sed porta eros. Cras id egestas sapien. Proin non metus eget felis eleifend adipiscing. Nunc malesuada pharetra blandit.</p>
  </div>
  <p class="letter-closing">Your sincerely</p>
</section>

<section class="sheet business-card">
  <div class="card-front">
    <div class="brand">
      <span class="brand-mark"></span>
      <span class="brand-name">Copper Glen Partners llc</span>
    </div>
  </div>
  <div class="card-details">
    <p class="card-name">Miles T Carver</p>
    <p class="card-title">CPA MST Principal</p>
    <p>842 East Marlow Avenue, Suite 7B<br>Chicago, Illinois 60617</p>
    <p class="contact-line"><b>Tel.</b> 312.555.0271</p>
    <p class="contact-line"><b>Fax.</b> 312.555.4186</p>
    <p class="contact-line"><b>Cell.</b> 312.555.0388</p>
    <p>milestcarver@copperglenpartnersllc.example</p>
    <p class="card-web">www.copperglenpartnersllc.example</p>
  </div>
</section>

<section class="sheet envelope">
  <div class="envelope-brand brand">
    <span class="brand-mark"></span>
    <span class="brand-name">Copper Glen Partners llc</span>
  </div>
  <p class="envelope-web">www.copperglenpartnersllc.example</p>
  <address class="envelope-return" style="font-style:normal">
    842 East Marlow Avenue, Suite 7B<br>
    Chicago, Illinois 60617<br>
    <span class="contact-line"><b>Tel.</b> 312.555.0271</span><br>
    <span class="contact-line"><b>Fax.</b> 312.555.4186</span>
  </address>
</section>

</body>
</html>
```